Book cover for book entitled "Planting Gardens After Winter ....Plus Growing Bright Mornings Within"

I need a book cover for ebook and 6" x 9" paperback print book (print forge pod). I want a simple but "positive" cover with no gothic or darkness in design. I would prefer a "hopeful color scheme" in yellow, blue, green analogous colors and very easy to read main title "Planting Gardens After Winter". I want the tag line of the title. "plus grow bright mornings within" included on the cover please. I am not opposed to white in the color scheme I believe the graphic needs to somehow deal with doors, blocks, keys (perhaps a combination lock since the book is my story of healing from pancreatic cancer through faith, nutrition, and lifestyle changes). I am basically looking for the front cover from you but in a high definition format so it can be transferred to posters and banners for seminar displays. I am uploading my photo in case a designer would want to include a small copy of it in a design although I plan the photo to be on the back cover. The photo could, of course, be cropped.

I would also be interested in seeing a design with a woman  with arms folded and looking satisfied or victorious (happy) casually leaning against a closed door.    It can be very simple....

This graphic could be photo or drawing-even a good line drawing.   Almost whimsical would be okay.  This cover need not be highly complicated but I do want the title easy to read in small or large sizes for ebook and print book.

Reason: I have just changed to "committed" and some new "acceptances" have just come in.

Industry/Entity Type

Nutrition

Font styles to use
Serif

Colors
fbee3e
acd037
33b7a4
34a6d8
3377b5

```html
<!DOCTYPE html>
<html lang="en">
<head>
<meta charset="utf-8">
<title>Planting Gardens After Winter</title>
<link rel="stylesheet" href="https://fonts.googleapis.com/css2?family=Bodoni+Moda:ital,opsz,wght@0,6..96,400;1,6..96,400&display=swap">
<style>
  :root {
    --sky: #e8f0fd;
    --ink: #555555;
    --gold: #e2bd74;
    --mint: #43d7b6;
  }
  html, body {
    margin: 0;
    padding: 0;
    overflow: hidden;
    background: var(--sky);
  }
  .cover {
    position: relative;
    width: 801px;
    height: 1200px;
    background: var(--sky);
    overflow: hidden;
    font-family: "Bodoni Moda", "Didot", serif;
    color: var(--ink);
  }
  .key-row {
    position: absolute;
    top: 70px;
    left: 0;
    width: 801px;
    height: 356px;
  }
  .key {
    position: absolute;
    top: 0;
    width: 126px;
    height: 356px;
    border-radius: 60px 60px 10px 10px;
    background: var(--gold);
  }
  .key--accent { background: var(--mint); }
  .title {
    position: absolute;
    top: 508px;
    left: 0;
    width: 801px;
    margin: 0;
    text-align: center;
    font-weight: 400;
    font-size: 100px;
    line-height: 128px;
    letter-spacing: 0.5px;
  }
  .title__line { display: block; white-space: nowrap; }
  .title__accent { color: var(--mint); }
  .tagline {
    position: absolute;
    top: 934px;
    left: 0;
    width: 801px;
    margin: 0;
    text-align: center;
    font-style: italic;
    font-size: 34px;
    line-height: 44px;
    color: var(--ink);
  }
  .author {
    position: absolute;
    top: 1118px;
    left: 0;
    width: 801px;
    margin: 0;
    text-align: center;
    font-size: 28px;
    line-height: 40px;
  }
</style>
</head>
<body>
  <main class="cover">
    <div class="key-row">
      <div class="key" style="left:0px" role="img" aria-label="Ornate antique gold key"></div>
      <div class="key" style="left:167px" role="img" aria-label="Ornate antique gold key"></div>
      <div class="key key--accent" style="left:337px" role="img" aria-label="Ornate antique key in mint green, standing out from the row"></div>
      <div class="key" style="left:503px" role="img" aria-label="Ornate antique gold key"></div>
      <div class="key" style="left:668px" role="img" aria-label="Ornate antique gold key"></div>
    </div>
    <h1 class="title">
      <span class="title__line">Planting</span>
      <span class="title__line">Gardens After</span>
      <span class="title__line title__accent">Winter</span>
    </h1>
    <p class="tagline">plus grow bright mornings within</p>
    <p class="author">Author Name</p>
  </main>
</body>
</html>
```